VELMOR Website Design

We need a website designed for our company VELMOR. We are a luxury lifestyle club that will provide benefits and services for our members. The site should be clean & sleek, preferably using black and white (or darker colors). (example sites: brastelle.com, fovix.com)

Here is a link of a sample page I did using wix. (https://dunmerel7.pagebuildr.com/mysite) This can be used to get a general idea.

Target Market(s)

Upper Middle Class in the United States

Number of Pages Required

5+ page

Font styles to use
Sans Serif
Other font styles liked:
• Arial (or other similar fonts)

Requirements
Must have
• A clean design that is eye-catching and speaks to our company.
Nice to have
• Ideas for copy.

```html
<!DOCTYPE html>
<html lang="en">
<head>
<meta charset="utf-8">
<title>VELMOR — Contact</title>
<link rel="stylesheet" href="https://fonts.googleapis.com/css2?family=Nunito+Sans:wght@300;400;600&display=swap">
<style>
  :root {
    --header-bg: #181818;
    --ink: #000000;
    --paper: #ffffff;
    --muted: #8a8a8a;
    --rule: #bdbdbd;
    --photo-dark: #0d0c0b;
    --photo-warm: #5a4630;
    --photo-blue: #1c2338;
  }
  * { box-sizing: border-box; margin: 0; padding: 0; }
  html, body { width: 1200px; height: 818px; overflow: hidden; }
  body {
    position: relative;
    background: var(--paper);
    font-family: "Nunito Sans", Arial, sans-serif;
    color: var(--paper);
  }
  .site-header {
    position: absolute; left: 0; top: 0; width: 1200px; height: 64px;
    background: var(--header-bg);
  }
  .brand {
    position: absolute; left: 236px; top: 14px;
    font-size: 28px; font-weight: 400; letter-spacing: 1px; line-height: 34px;
  }
  .main-nav a {
    position: absolute; top: 24px;
    font-size: 12.5px; font-weight: 400; line-height: 16px;
    color: var(--paper); text-decoration: none; letter-spacing: 0.2px;
  }
  .hero-photo {
    position: absolute; left: 0; top: 64px; width: 598px; height: 618px;
    background:
      radial-gradient(ellipse at 45% 55%, rgba(120,95,60,0.35), transparent 55%),
      linear-gradient(100deg, var(--photo-blue) 0%, var(--photo-warm) 30%, var(--photo-dark) 55%, #2a241c 80%, var(--photo-warm) 100%);
  }
  .contact-panel {
    position: absolute; left: 539px; top: 138px; width: 597px; height: 472px;
    background: var(--ink);
  }
  .contact-title {
    position: absolute; left: 0; top: 58px; width: 100%;
    text-align: center; font-size: 27px; font-weight: 400; line-height: 26px;
    padding-left: 150px; padding-right: 0;
  }
  .contact-title span { display: block; width: 302px; margin-left: 0; }
  .field {
    position: absolute; left: 171px; width: 260px;
    border-bottom: 1px solid var(--rule);
    font-size: 11.5px; color: var(--muted); padding-left: 8px;
  }
  .send-button {
    position: absolute; left: 226px; top: 393px; width: 150px; height: 23px;
    border-radius: 12px; background: var(--paper); color: var(--ink);
    font-size: 12px; line-height: 23px; text-align: center;
  }
  .site-footer {
    position: absolute; left: 0; top: 682px; width: 1200px; height: 136px;
    background: var(--ink);
  }
  .social-links { position: absolute; top: 50px; left: 504px; display: flex; gap: 6px; }
  .social-links span {
    width: 22px; height: 22px; border-radius: 3px; background: var(--paper); display: block;
  }
  .copyright {
    position: absolute; top: 100px; width: 100%; text-align: center; font-size: 12px;
  }
</style>
</head>
<body>
  <header class="site-header">
    <div class="brand">VELMOR</div>
    <nav class="main-nav">
      <a style="left:502px">HOME</a>
      <a style="left:570px">ABOUT</a>
      <a style="left:645px">SERVICES AND BENEFITS</a>
      <a style="left:821px">APPLY</a>
      <a style="left:888px">CONTACT US</a>
    </nav>
  </header>

  <div class="hero-photo" role="img" aria-label="Dimly lit subway station platform curving into a tunnel beside the tracks"></div>

  <section class="contact-panel">
    <h1 class="contact-title" style="padding:0;left:0">
      <span style="width:100%">WE'RE ALWAYS HERE,</span>
      <span style="width:100%">DROP US A LINE!</span>
    </h1>
    <div class="field" style="top:142px;height:22px">Fullname</div>
    <div class="field" style="top:180px;height:22px">Email</div>
    <div class="field" style="top:222px;height:22px">Subject</div>
    <div class="field" style="top:321px;height:23px">Message</div>
    <div class="send-button">Send</div>
  </section>

  <footer class="site-footer">
    <div class="social-links" aria-label="Social links">
      <span></span><span></span><span></span><span></span><span></span><span></span><span></span>
    </div>
    <p class="copyright">© 2018 VELMOR</p>
  </footer>
</body>
</html>
```